Flyer for an pediatric sleep consultancy - to distribute to play and childcare centers etc.

I need a flyer that will attract the attention of parents with children between the age of babies to toddlers, who may be experiencing sleep issues. The flyer will be placed at places such as community centers, doctors room, play centers, kindergardens, etc.

My company is called "The Quiet Meadow Nest" and provides a sleep consultancy service. My service essentially provides a customized plan for parents to follow and general advice and guidance. It is not medical advice.

I like to the flyer to have an overall tone that is soft and peaceful with a clean and beautiful design, however can catch the attention of parents who may be struggling with their child's sleep issues and are sleep deprived. I would like photos with minimal text. The colour I use is a brownish rose. I will attach some of my designs to give you an idea. You can have a look at my homepage as well to get an idea about my esthetic direction and the colour. Although the colour of my page is a bit too brownish....

I will provide the text to appear in the flyer once I have a better idea of the layout that I prefer for the flyer. The text however wont be extensive, just some catchy points.

I want to direct people to my website which is www.thequietmeadownest.example
I offer a first FREE evaluation call, to the parents, to get to know each other better, learn about their child's particular sleep problems and see if we are a good fit and can work together. I would like to have this information somehow on the flyer, so that the parents will contact me.
I also have a facebook page, which is: The Quiet Meadow Nest

I have a logo that I would like to appear on the flyer. I will attach the file once the uploader on pixel fair is fixed.

When I print the flyer - I like to print A5 SIZE ... please make sure the formatting is OK for this size.

Here are some text ideas. of course all of it would be too much, I guess. On the front of the flyer I would like to have some catchy phrase or something similar to get people interested and to want to know more. On the back there could be a bit more text and information. But I'm open too suggestions....
I'm not too sure about the wording yet. But here are some text that I might be use:

Is sleep an issue in your home?

Is your baby having trouble sleeping? ... are you?!
I can help!

Sleep, baby, sleep….

Teaching children how to sleep

The Quiet Meadow Nest is a pediatric sleep consultancy that specializes in helping parents with children who struggle to develop good and healthy sleep habits.
Disruptive sleep patterns or not enough sleep can affect the physical, mental and emotional development of your child.

Of course nobody plans to have a sleep problem, but habits can become easily ingrained and spiral quickly out of control and you can find yourself sleep deprived, desperate and not too sure what to do. You see all the other sleeping babies and wish there was someone who understood what you were going through?! Well, there is!

Contact me for a free 15 minute consultation.

This 15 minute „mini“ consultation is a chance to discuss your unique sleep challenges and sleep goals with me. I will provide you with an overview of how I will work with your family to achieve your wildest sleep dreams (goals).
Furthermore do I understand and believe that every child and their family is unique and there is no one size fits all!
I would love to have a chat with you and talk about how I can help make things easier for you and your family!

Do I need a sleep consultant for my child?
The answer is yes if:
- if your child will only fall asleep when nursing or bottle feeding
- if your child needs a dummy or other external aid, like being rocked, patted or taken for a care ride to fall asleep
- if your good night routine is a challenging and exhausting procedure instead of a relaxed and enjoyable moment for the whole family
- if sleep is a constant battle in your home which leaves you feeling frustrated and exhausted
- if your own lack of sleep is taking a toll on you and the whole family

What can I do for you?

I will:

- Guide you to set an age appropriate foundation for good sleep
- Create an individual sleep plan tailored especially to your child’s sleep needs and circumstances
- Help you to teach your childto go to sleep and get back to sleep independently during the night
- show you how to teach your child to take healthful, restorative naps
-Learn

Contact:

Marta Lindqvist
info@thequietmeadownest.example
www.thequietmeadownest.example
+34 612 384 570

Consultations in English, German or Spanish via Phone/Skype or home consultation

Reason: I have to go on a business trip and won't be able to choose a design until the deadline. During the trip I won't have time to give feedback and ask for changes. thank you

Target Market(s)

parents, sleep deprived mothers, young families, child care provider,

Industry/Entity Type

Baby Care

Contact Information for Business Card

Marta Lindqvist
pediatric sleep consultant
+34 612 384 570

```html
<!DOCTYPE html>
<html lang="en">
<head>
<meta charset="utf-8">
<title>The Quiet Meadow Nest – Flyer</title>
<link rel="stylesheet" href="https://fonts.googleapis.com/css2?family=Kreon:wght@300;400&family=Lato:ital,wght@0,400;0,700;1,400&family=Oswald:wght@400;500&display=swap">
<style>
:root{
  --rose:#c4806f;
  --rose-light:#e3bcb1;
  --sage:#5d7a6f;
  --sage-ring:#7f9189;
  --mist:#eceeed;
  --ink:#2f2f2f;
  --paper:#ffffff;
  --backdrop:#efefef;
}
*{margin:0;padding:0;box-sizing:border-box}
html,body{width:1200px;height:1200px;overflow:hidden;background:var(--backdrop)}
body{position:relative;font-family:'Lato',sans-serif;color:var(--ink)}
.page{position:absolute;top:260px;width:463px;height:647px;background:var(--paper);overflow:hidden;box-shadow:0 2px 8px rgba(0,0,0,.25)}
.front{left:109px}
.back{left:628px}
.abs{position:absolute}
.shapes{position:absolute;left:0;top:0;width:463px;height:647px}
.photo{position:absolute}

/* front */
.hero-photo{left:0;top:0;width:463px;height:250px;background:linear-gradient(120deg,#f3ede9 0%,#ecdcd6 45%,#e9d3cc 70%,#f1e6e1 100%)}
.headline{left:35px;top:22px;font-family:'Kreon',serif;font-weight:300;font-size:35px;line-height:38px}
.headline .l1{color:var(--rose);display:block}
.headline .l2{color:var(--sage);display:block}
.front-brand{left:22px;top:270px;display:flex;align-items:center;gap:7px;font-family:'Lato',sans-serif;font-size:15px;color:var(--sage)}
.dot{width:10px;height:10px;border-radius:50%;background:var(--rose)}
.badge{left:291px;top:195px;width:164px;height:164px;border-radius:50%;background:var(--rose);border:6px solid #fff;box-shadow:0 3px 8px rgba(0,0,0,.2);color:#fff;text-align:center;font-family:'Oswald',sans-serif}
.badge .free{display:block;margin-top:24px;font-size:46px;line-height:50px;font-weight:500}
.badge .call{display:block;font-size:23px;line-height:28px}
.parent-photo{left:273px;top:353px;width:170px;height:294px;border-radius:80px 80px 0 0;background:linear-gradient(180deg,#eadcd2 0%,#c9b7aa 35%,#5a5a5c 65%,#8a8f99 100%)}
.kicker{left:39px;top:350px;font-family:'Kreon',serif;font-weight:300;font-size:13px;line-height:15px;color:var(--sage);letter-spacing:.3px}
.title{left:39px;top:366px;font-family:'Kreon',serif;font-weight:300;font-size:26px;line-height:28px;color:var(--rose);letter-spacing:.5px}
.intro{left:39px;top:401px;width:208px;font-size:11px;line-height:12.7px;text-align:justify}
.intro p+p{margin-top:7px}
.front-contact{left:39px;top:528px}
.contact-head{font-family:'Kreon',serif;font-weight:300;font-size:19px;line-height:20px;color:var(--rose)}
.contact-name{font-family:'Kreon',serif;font-weight:300;font-size:18px;line-height:20px;color:var(--sage);margin-top:5px}
.contact-list{list-style:none;margin-top:4px;margin-left:-15px}
.contact-list li{display:flex;align-items:center;gap:7px;font-size:13px;line-height:19px}
.icon{width:8px;height:8px;flex:none}

/* back */
.back-brand{left:0;top:58px;width:463px;display:flex;justify-content:center;align-items:center;gap:7px;font-size:15px;color:var(--sage)}
.pill{left:34px;top:104px;width:401px;height:30px;border-radius:15px;background:var(--rose);color:#fff;font-size:18px;font-weight:700;text-align:center;line-height:30px;letter-spacing:.2px;box-shadow:0 1px 2px rgba(0,0,0,.2)}
.offer{left:28px;top:142px;width:418px;font-size:7.7px;line-height:11.5px}
.mist{left:0;top:199px;width:463px;height:330px;background:linear-gradient(180deg,#eef0ef 0%,#e6e9e8 60%,#f4f4f4 100%)}
.col{top:215px;width:180px}
.col-left{left:33px}
.col-right{left:257px;width:180px}
.col h3{font-weight:400;font-size:10.5px;line-height:12.5px;color:var(--sage)}
.col h4{font-weight:400;font-style:italic;font-size:10px;color:var(--sage);margin:6px 0 3px}
.col ul{list-style:none}
.col li{position:relative;padding-left:8px;font-style:italic;font-size:7.3px;line-height:10px}
.col-left li{text-align:justify}
.col-right li{line-height:13.7px}
.col li::before{content:"";position:absolute;left:0;top:4px;width:3px;height:3px;border-radius:50%;background:var(--rose)}
.divider{left:231px;top:218px;width:1px;height:158px;background:#b9c1bd}
.ring{position:absolute;border-radius:50%;border:5px solid var(--sage-ring);box-shadow:0 2px 4px rgba(0,0,0,.15)}
.ring-a{left:68px;top:428px;width:108px;height:108px;background:linear-gradient(135deg,#f4ddd4,#dcb2a4)}
.ring-b{left:162px;top:389px;width:134px;height:134px;background:linear-gradient(135deg,#eadbd3,#f7f3f1)}
.ring-c{left:290px;top:423px;width:108px;height:108px;background:linear-gradient(135deg,#f7efe9,#e8d4c9)}
.back-contact{left:0;top:534px;width:463px;text-align:center}
.back-contact .contact-head{font-size:18px}
.back-contact .contact-name{font-size:13.5px;margin-top:0;font-family:'Lato',sans-serif;font-weight:400}
.back-rows{left:42px;top:583px;width:400px;display:flex}
.back-rows ul{list-style:none}
.back-rows li{display:flex;align-items:flex-start;gap:5px;font-size:10.5px;line-height:13.5px}
.back-rows li .icon{margin-top:3px}
.back-rows .left{width:176px}
.back-rows .sep{width:1px;height:38px;background:#b9c1bd;margin:0 29px 0 0}
</style>
</head>
<body>

<section class="page front">
  <div class="photo hero-photo" role="img" aria-label="Close-up photo of a peacefully sleeping baby with tiny hands near its face"></div>
  <svg class="shapes" viewBox="0 0 463 647" aria-hidden="true">
    <path d="M0,228 C120,205 270,204 463,214 L463,647 L0,647 Z" fill="#ffffff"/>
    <path d="M0,228 C120,205 270,204 463,214 L463,232 C270,222 120,224 0,248 Z" fill="var(--sage)"/>
    <path d="M0,300 C100,322 220,324 320,300 L320,308 C220,334 100,334 0,312 Z" fill="var(--rose-light)"/>
    <path d="M0,512 C100,492 220,488 300,498 C370,506 420,522 463,540 L463,647 L0,647 Z" fill="#ffffff"/>
    <path d="M0,512 C100,492 220,488 300,498 C370,506 420,522 463,540 L463,550 C420,532 370,516 300,508 C220,500 100,504 0,522 Z" fill="var(--rose-light)"/>
  </svg>
  <h1 class="abs headline"><span class="l1">Sleep, Baby,</span><span class="l2">Sleep...</span></h1>
  <div class="abs front-brand"><span class="dot"></span>The Quiet Meadow Nest</div>
  <div class="photo parent-photo" role="img" aria-label="Photo of the sleep consultant smiling and holding a toddler"></div>
  <div class="abs badge"><span class="free">FREE</span><span class="call">Evaluation Call</span></div>
  <p class="abs kicker">TEACHING CHILDREN</p>
  <h2 class="abs title">HOW TO SLEEP</h2>
  <div class="abs intro">
    <p>The Quiet Meadow Nest is a pediatric sleep consultancy that specializes in helping parents with children who struggle to develop good and healthy sleep habits.</p>
    <p>Disruptive sleep patterns or not enough sleep can affect the physical, mental and emotional development of your child.</p>
  </div>
  <div class="abs front-contact">
    <p class="contact-head">Contact Us:</p>
    <p class="contact-name">Marta Lindqvist</p>
    <ul class="contact-list">
      <li><svg class="icon" viewBox="0 0 10 10"><rect x="0.5" y="2" width="9" height="6.5" fill="none" stroke="var(--rose)" stroke-width="1.2"/><path d="M0.5,2 L5,6 L9.5,2" fill="none" stroke="var(--rose)" stroke-width="1.2"/></svg>info@thequietmeadownest.example</li>
      <li><svg class="icon" viewBox="0 0 10 10"><circle cx="5" cy="5" r="4.2" fill="none" stroke="var(--rose)" stroke-width="1.2"/><path d="M1,5 H9 M5,1 C3,3.5 3,6.5 5,9 M5,1 C7,3.5 7,6.5 5,9" fill="none" stroke="var(--rose)" stroke-width="0.9"/></svg>www.thequietmeadownest.example</li>
      <li><svg class="icon" viewBox="0 0 10 10"><path d="M2,0.8 L3.8,2.8 L2.8,4 C3.5,5.6 4.6,6.7 6,7.3 L7.2,6.2 L9.2,8 L8,9.4 C4.5,9 1,5.5 0.6,2 Z" fill="var(--rose)"/></svg>+34 612 384 570</li>
    </ul>
  </div>
</section>

<section class="page back">
  <div class="abs back-brand"><span class="dot"></span>The Quiet Meadow Nest</div>
  <div class="abs pill">Contact me for a free 15 minute consultation</div>
  <p class="abs offer">This 15 minute „mini“ consultation is a chance to discuss your unique sleep challenges and sleep goals with me. I will provide you with an overview of how I will work with your family to achieve your wildest sleep dreams (goals). Furthermore do I understand and believe that every child and their family is unique and there is no one size fits all! I would love to have a chat with you and talk about how I can help make things easier for you and your family!</p>
  <div class="photo mist" role="img" aria-label="Soft faded photo of a sleeping baby as background"></div>
  <div class="abs col col-left">
    <h3>Do I need a sleep consultant<br>for my child?</h3>
    <h4>The answer is yes if:</h4>
    <ul>
      <li>If your child will only fall asleep when nursing or bottle feeding</li>
      <li>If your child needs a dummy or other external aid, like being rocked, patted or taken for a care ride to fall asleep</li>
      <li>If your good night routine is a challenging and exhausting procedure instead of a relaxed and enjoyable moment for the whole family</li>
      <li>If sleep is a constant battle in your home which leaves you feeling frustrated and exhausted</li>
      <li>If your own lack of sleep is taking a toll on you and the whole family</li>
    </ul>
  </div>
  <div class="abs divider"></div>
  <div class="abs col col-right">
    <h3>What can I do for you?</h3>
    <h4>I will</h4>
    <ul>
      <li>Guide you to set an age appropriate foundation for good sleep</li>
      <li>Create an individual sleep plan tailored especially to your child’s sleep needs and circumstances</li>
      <li>Help you to teach your child to go to sleep and get back to sleep independently during the night</li>
      <li>Show you how to teach your child to take healthful, restorative naps</li>
      <li>Learn</li>
    </ul>
  </div>
  <svg class="shapes" viewBox="0 0 463 647" aria-hidden="true">
    <path d="M0,490 C80,470 150,462 230,470 C310,478 390,470 463,482 L463,505 C390,495 310,502 230,500 C150,498 80,500 0,512 Z" fill="var(--rose-light)"/>
    <path d="M0,512 C80,500 150,498 230,500 C310,502 390,495 463,505 L463,647 L0,647 Z" fill="#ffffff"/>
  </svg>
  <div class="ring ring-a" role="img" aria-label="Photo of a baby's small hands"></div>
  <div class="ring ring-c" role="img" aria-label="Photo of a toddler asleep on a white pillow"></div>
  <div class="ring ring-b" role="img" aria-label="Photo of two young siblings sleeping side by side"></div>
  <div class="abs back-contact">
    <p class="contact-head">Contact Us:</p>
    <p class="contact-name">Marta Lindqvist</p>
  </div>
  <div class="abs back-rows">
    <ul class="left">
      <li><svg class="icon" viewBox="0 0 10 10"><path d="M2,0.8 L3.8,2.8 L2.8,4 C3.5,5.6 4.6,6.7 6,7.3 L7.2,6.2 L9.2,8 L8,9.4 C4.5,9 1,5.5 0.6,2 Z" fill="var(--rose)"/></svg>+34 612 384 570</li>
      <li><svg class="icon" viewBox="0 0 10 10"><path d="M5,9.8 C2,6 1.5,4.8 1.5,3.6 A3.5,3.5 0 0 1 8.5,3.6 C8.5,4.8 8,6 5,9.8 Z" fill="var(--rose)"/><circle cx="5" cy="3.6" r="1.3" fill="#fff"/></svg>Carrer de les Violetes 14<br>08012 Barcelona</li>
    </ul>
    <div class="sep"></div>
    <ul>
      <li><svg class="icon" viewBox="0 0 10 10"><rect x="0.5" y="2" width="9" height="6.5" fill="none" stroke="var(--rose)" stroke-width="1.2"/><path d="M0.5,2 L5,6 L9.5,2" fill="none" stroke="var(--rose)" stroke-width="1.2"/></svg>info@thequietmeadownest.example</li>
      <li><svg class="icon" viewBox="0 0 10 10"><circle cx="5" cy="5" r="4.2" fill="none" stroke="var(--rose)" stroke-width="1.2"/><path d="M1,5 H9 M5,1 C3,3.5 3,6.5 5,9 M5,1 C7,3.5 7,6.5 5,9" fill="none" stroke="var(--rose)" stroke-width="0.9"/></svg>www.thequietmeadownest.example</li>
    </ul>
  </div>
</section>

</body>
</html>
```